Carver Lindqvist Group Business Cards

We have a new logo, and want to design new business cards with it. We are 21 years in business, and want a fresh but professional look, so not a lot of extra stuff on the card. We are a recruiting and staffing firm focused on placing accounting and finance professionals in the Dallas TX area. I've attached our new logo that should be displayed on the cards. Here is what I think we want on the cards:
Ray Pemberly, CPA
Partner and Managing Director
8282 Orchard Vale Rd.
Suite 610
Dallas, TX 75391
O 214-555-0184
M 214-555-0237
ray@carverlindqvist.example
www.carverlindqvist.example

```html
<!DOCTYPE html>
<html lang="en">
<head>
<meta charset="utf-8">
<title>Carver Lindqvist Group – Business Cards</title>
<link rel="stylesheet" href="https://fonts.googleapis.com/css2?family=Montserrat:wght@500;700&family=Arimo:wght@400&display=swap">
<style>
  :root {
    --brand-blue: #233f94;
    --brand-blue-light: #4a6cc4;
    --ink: #1f2433;
    --paper: #ffffff;
    --backdrop: #e4e6ea;
  }
  * { box-sizing: border-box; margin: 0; padding: 0; }
  html, body { width: 1200px; height: 902px; overflow: hidden; }
  body {
    background: var(--backdrop);
    display: flex;
    flex-direction: column;
    align-items: center;
    justify-content: center;
    gap: 40px;
    font-family: "Arimo", Arial, sans-serif;
  }
  .card {
    position: relative;
    width: 700px;
    height: 400px;
    overflow: hidden;
    box-shadow: 0 6px 18px rgba(0,0,0,0.18);
  }

  /* Back side */
  .card-back {
    background: var(--brand-blue);
    color: var(--paper);
    display: flex;
    flex-direction: column;
    align-items: center;
    justify-content: center;
  }
  .card-back .wordmark {
    font-family: "Montserrat", Arial, sans-serif;
    font-weight: 700;
    font-size: 34px;
    letter-spacing: 0.5px;
    text-transform: uppercase;
  }
  .card-back .wordmark-rule {
    width: 420px;
    height: 2px;
    background: var(--paper);
    margin-top: 14px;
  }
  .card-back .website {
    position: absolute;
    bottom: 62px;
    font-family: "Montserrat", Arial, sans-serif;
    font-weight: 500;
    font-size: 13px;
    letter-spacing: 3px;
    text-transform: uppercase;
  }

  /* Front side */
  .card-front { background: var(--paper); color: var(--ink); }
  .card-front .wordmark {
    position: absolute;
    top: 58px;
    right: 48px;
    font-family: "Montserrat", Arial, sans-serif;
    font-weight: 700;
    font-size: 26px;
    color: var(--brand-blue);
    text-transform: uppercase;
  }
  .card-front .wordmark-rule {
    position: absolute;
    top: 102px;
    right: 48px;
    width: 330px;
    height: 2px;
    background: var(--brand-blue);
  }
  .card-front .divider {
    position: absolute;
    top: 200px;
    left: 48px;
    right: 48px;
    height: 1.5px;
    background: var(--brand-blue);
  }
  .address {
    position: absolute;
    top: 126px;
    right: 48px;
    text-align: right;
    font-size: 17px;
    line-height: 1.35;
    color: var(--ink);
  }
  .person { position: absolute; top: 218px; left: 48px; }
  .person .name {
    font-family: "Montserrat", Arial, sans-serif;
    font-weight: 700;
    font-size: 22px;
    color: var(--brand-blue);
    text-transform: uppercase;
  }
  .person .title {
    font-size: 17px;
    color: var(--brand-blue-light);
    margin-top: 2px;
  }
  .contacts {
    position: absolute;
    top: 284px;
    left: 48px;
    list-style: none;
    font-size: 17px;
    line-height: 22px;
  }
  .contacts li { display: flex; align-items: center; gap: 14px; }
  .contacts svg { width: 16px; height: 16px; flex: none; }
  .contacts .note { color: var(--brand-blue-light); }
  .bottom-band { position: absolute; left: 0; bottom: 0; width: 700px; height: 36px; }
</style>
</head>
<body>

<section class="card card-back" aria-label="Card back">
  <div class="wordmark">Carver Lindqvist Group</div>
  <div class="wordmark-rule"></div>
  <div class="website">www.carverlindqvist.example</div>
</section>

<section class="card card-front" aria-label="Card front">
  <div class="wordmark">Carver Lindqvist Group</div>
  <div class="wordmark-rule"></div>

  <address class="address" style="font-style:normal">
    8282 Orchard Vale Rd.<br>Suite 610<br>Dallas, TX 75391
  </address>

  <div class="divider"></div>

  <div class="person">
    <div class="name">Ray Pemberly, CPA</div>
    <div class="title">Partner and Managing Director</div>
  </div>

  <ul class="contacts">
    <li>
      <svg viewBox="0 0 16 16" aria-hidden="true"><rect x="4" y="1" width="8" height="14" rx="1.5" fill="none" stroke="#233f94" stroke-width="1.6"/><circle cx="8" cy="12.5" r="0.9" fill="#233f94"/></svg>
      <span>214-555-0237</span>
    </li>
    <li>
      <svg viewBox="0 0 16 16" aria-hidden="true"><path d="M3 2.5l2.6-.6 1.4 3-1.6 1.2a8 8 0 0 0 4.5 4.5l1.2-1.6 3 1.4-.6 2.6C8 13.6 2.4 8 3 2.5z" fill="#233f94"/></svg>
      <span>214-555-0184 <span class="note">(Office)</span></span>
    </li>
    <li>
      <svg viewBox="0 0 16 16" aria-hidden="true"><rect x="1.5" y="3.5" width="13" height="9" fill="none" stroke="#233f94" stroke-width="1.5"/><path d="M1.5 3.5L8 9l6.5-5.5" fill="none" stroke="#233f94" stroke-width="1.5"/></svg>
      <span>ray@carverlindqvist.example</span>
    </li>
    <li>
      <svg viewBox="0 0 16 16" aria-hidden="true"><circle cx="8" cy="8" r="6.5" fill="none" stroke="#233f94" stroke-width="1.4"/><ellipse cx="8" cy="8" rx="2.8" ry="6.5" fill="none" stroke="#233f94" stroke-width="1.2"/><path d="M1.5 8h13M2.5 4.8h11M2.5 11.2h11" stroke="#233f94" stroke-width="1.1"/></svg>
      <span>www.carverlindqvist.example</span>
    </li>
  </ul>

  <svg class="bottom-band" viewBox="0 0 700 36" aria-hidden="true">
    <rect x="0" y="22" width="700" height="14" fill="#233f94"/>
    <polygon points="380,36 420,0 700,0 700,36" fill="#233f94"/>
    <polygon points="420,0 700,0 700,22 444,22 440,14" fill="#4a6cc4"/>
    <line x1="404" y1="36" x2="444" y2="0" stroke="#ffffff" stroke-width="3"/>
  </svg>
</section>

</body>
</html>
```